Business Card Design

I am a Accounting/Bookkeeping company.  As a sideline, I am also a Notary so I would like that somewhere, either in front or perhaps the backside for the notary business.
I found a standard card I really like but didn't like the "little man" standing on the scale.
I love the colors so I am wondering if you would be able to duplicate this without the man and perhaps money or something appropriate on this side of scale
I also need help on the font.  I tend to like feminine styles but am told they are too hard to read.

Target Market(s)
Small businesses, Individuals
Industry/Entity Type
Business
Contact Information for Business Card
The Tidy Ledgerwright
Balancing your books is our specialty
Marisol (Pebbleton) Varnaccio
Accounting Associate
Certified FiscalTrail CountExpert
Notary Public
Serving Sonoma County                            415-362-9184
marisol.varnaccio@plumpost.example

Requirements
Must have
- I would like a glossy card

```html
<!DOCTYPE html>
<html lang="en">
<head>
<meta charset="utf-8">
<title>The Tidy Ledgerwright — Business Card</title>
<link rel="stylesheet" href="https://fonts.googleapis.com/css2?family=Cinzel:wght@400;600&display=swap">
<style>
  :root {
    --page-bg: #e9e8ee;
    --card-deep: #241660;
    --card-mid: #2c2a8c;
    --card-bright: #3a4cb8;
    --ink-light: #ffffff;
    --emblem-tone: rgba(255, 255, 255, 0.16);
  }
  html, body {
    margin: 0;
    padding: 0;
    width: 1200px;
    height: 892px;
    overflow: hidden;
    background: var(--page-bg);
  }
  .stage {
    width: 1200px;
    height: 892px;
    display: flex;
    align-items: center;
    justify-content: center;
  }
  .business-card {
    position: relative;
    width: 1000px;
    height: 572px;
    background: linear-gradient(120deg, var(--card-deep) 0%, var(--card-mid) 50%, var(--card-bright) 100%);
    color: var(--ink-light);
    font-family: "Cinzel", "Times New Roman", serif;
    box-shadow: 0 18px 40px rgba(20, 14, 60, 0.35);
    overflow: hidden;
  }
  .business-card::after {
    content: "";
    position: absolute;
    inset: 0;
    background: linear-gradient(160deg, rgba(255,255,255,0.10) 0%, rgba(255,255,255,0) 40%);
    pointer-events: none;
  }
  .brand-name {
    position: absolute;
    left: 70px;
    top: 42px;
    margin: 0;
    font-size: 50px;
    font-weight: 600;
    letter-spacing: 1px;
  }
  .tagline {
    position: absolute;
    left: 150px;
    top: 106px;
    margin: 0;
    font-size: 23px;
    letter-spacing: 1.5px;
  }
  .credentials {
    position: absolute;
    left: 150px;
    top: 178px;
    margin: 0;
    font-size: 22px;
    line-height: 1.2;
  }
  .credentials p { margin: 0; }
  .credentials .gap { margin-top: 18px; }
  .scale-emblem {
    position: absolute;
    left: 600px;
    top: 215px;
    width: 250px;
    height: 215px;
    border-radius: 12px;
    background: var(--emblem-tone);
  }
  .service-area {
    position: absolute;
    left: 40px;
    top: 440px;
    margin: 0;
    font-size: 24px;
  }
  .contact {
    position: absolute;
    right: 45px;
    top: 462px;
    margin: 0;
    text-align: right;
    font-size: 19px;
    line-height: 1.45;
  }
  .contact p { margin: 0; }
</style>
</head>
<body>
  <main class="stage">
    <article class="business-card">
      <h1 class="brand-name">The Tidy Ledgerwright</h1>
      <p class="tagline">Balancing your books is our specialty</p>

      <div class="credentials">
        <p>Marisol (Pebbleton) Varnaccio</p>
        <p>Accounting Associate</p>
        <p class="gap">Certified FiscalTrail CountExpert</p>
        <p>Notary Public</p>
      </div>

      <div class="scale-emblem" role="img" aria-label="White balance scale emblem"></div>

      <p class="service-area">Serving Sonoma County</p>

      <div class="contact">
        <p>T: 415 362 9184</p>
        <p>marisol.varnaccio@plumpost.example</p>
      </div>
    </article>
  </main>
</body>
</html>
```